The Harbourlight CV consultant

The service is premium. It is aimed at people 18-30, so students and those looking to change their first job, principally in the UK but also global. It is offering a very personalised CV writing service and is much more expensive than others on offer. I am very keen that it should look simple and premium. It needs to look very professional, reflecting the aspirational jobs that the clients will be applying for.
If there were three words that summed it up: modern, clean, premium.
I am waiting for all the testimonials to come in but they need to form a major part of the website.
I am also waiting for the full logo design files so that I can upload them. In the meantime there is a copy of the logo.
Thoughts to help those yet to send a design...
This is a premium service and some of the designs have looked very generic. The focus needs to be on quality and the process mentioned in the brief. The partnership and the advantages it brings are crucial but few have mentioned that.

```html
<!DOCTYPE html>
<html lang="en">
<head>
<meta charset="utf-8">
<title>The Harbourlight CV Consultant</title>
<link rel="stylesheet" href="https://fonts.googleapis.com/css2?family=Cinzel:wght@400;500&family=Montserrat:ital,wght@0,400;0,500;0,600;1,400&family=Allura&display=swap">
<style>
:root{
  --blue:#1a6fba;
  --band:#4a93c9;
  --ink:#2b2b2b;
  --text:#444;
  --white:#fff;
  --grey-circle:#8e8d92;
  --slate-circle:#8fa7b3;
  --sky-circle:#4f9ad0;
}
*{box-sizing:border-box;margin:0;padding:0}
html,body{width:1200px;height:3141px;overflow:hidden;background:var(--white)}
body{font-family:'Montserrat',sans-serif;color:var(--text);position:relative}
.abs{position:absolute}
/* header */
.logo{font-family:'Cinzel',serif;color:var(--blue);font-weight:500;font-size:17px;line-height:19px;letter-spacing:.5px}
.nav{left:421px;top:42px;display:flex;gap:17px;font-family:'Cinzel',serif;font-size:16px;color:var(--ink)}
.nav .active{color:var(--blue)}
.btn{background:var(--blue);color:var(--white);font-weight:600;border-radius:30px;display:flex;align-items:center;justify-content:center;text-transform:uppercase}
.header-btn{left:804px;top:26px;width:184px;height:54px;font-size:16px}
.signin{left:1010px;top:44px;color:var(--blue);font-weight:600;font-size:16px;display:flex;align-items:center;gap:5px}
/* hero */
.hero{left:0;top:110px;width:1200px;height:572px;background:linear-gradient(90deg,#7a7a7a 0%,#b9b9b9 30%,#8f8f8f 55%,#c4c4c4 80%,#9a9a9a 100%)}
.bubble{background:var(--white);border-left:6px solid var(--blue);border-radius:8px;padding:0 22px 0 22px;display:flex;align-items:center;font-weight:500;font-size:18px;line-height:25px;color:var(--ink);height:95px}
/* intro */
.name{left:0;width:1200px;top:764px;text-align:center;font-family:'Cinzel',serif;font-size:46px;color:var(--ink)}
.script{left:0;width:1200px;top:818px;text-align:center;font-family:'Allura',cursive;font-size:62px;color:#555}
.intro{left:160px;width:880px;top:928px;text-align:center;font-size:16.5px;line-height:26px}
.intro p{margin-bottom:25px}
.pillar{width:208px;height:208px;border-radius:50%}
.pillar-label{width:180px;text-align:center;font-weight:500;font-size:22px;line-height:28px;color:var(--ink)}
.outro{left:190px;width:820px;top:1694px;text-align:center;font-size:16.5px;line-height:26px}
/* testimonials */
.band{left:0;top:1857px;width:1200px;height:483px;background:var(--band);overflow:hidden}
.band h2{position:absolute;top:74px;width:1200px;text-align:center;font-family:'Cinzel',serif;font-weight:500;font-size:48px;color:var(--white)}
.card{position:absolute;top:170px;width:312px;height:209px;background:rgba(255,255,255,.13);border-radius:8px;padding:22px 20px;color:var(--white)}
.card q{display:block;font-style:italic;font-size:18px;line-height:24px;quotes:"\201C\00a0" "\201D"}
.card .by{margin-top:20px;font-size:16px}
.card .by b{font-weight:600}
.next{position:absolute;left:1076px;top:253px;width:44px;height:44px;border-radius:50%;background:var(--white);display:flex;align-items:center;justify-content:center}
/* partnership */
.partner{left:0;top:2340px;width:1200px;height:670px;background:linear-gradient(90deg,#f3f5f8 0%,#eef1f5 40%,#c9d0da 60%,#7f8fa6 80%,#5d6f8c 100%)}
.partner h2{position:absolute;left:112px;top:84px;font-family:'Cinzel',serif;font-weight:500;font-size:48px;color:var(--ink)}
.partner .copy{position:absolute;left:110px;top:164px;width:480px;font-size:17px;line-height:26px}
.partner .copy p{margin-bottom:25px}
.partner-btn{left:111px;top:516px;width:250px;height:64px;font-size:18px}
/* footer */
.copyright{left:420px;top:3065px;font-size:16px;color:var(--ink)}
.social{width:36px;height:36px;border-radius:50%;border:1.5px solid var(--blue)}
</style>
</head>
<body>

<header>
  <div class="abs logo" style="left:112px;top:33px">THE HARBOURLIGHT<br>CV CONSULTANT</div>
  <nav class="abs nav">
    <span class="active">HOME</span><span>ABOUT</span><span>SERVICES</span><span>TESTIMONIALS</span>
  </nav>
  <div class="abs btn header-btn">Contact me now</div>
  <div class="abs signin">
    <svg width="12" height="14" viewBox="0 0 12 14"><circle cx="6" cy="4" r="3.3" fill="#1a6fba"/><path d="M0 14c0-4 2.5-6 6-6s6 2 6 6z" fill="#1a6fba"/></svg>
    SIGN IN
  </div>
</header>

<section class="abs hero" role="img" aria-label="Black and white photo of a young woman working on a laptop"></section>
<div class="abs bubble" style="left:126px;top:190px;width:350px">Do you want to create a CV that stands out from the crowd?</div>
<div class="abs bubble" style="left:745px;top:190px;width:340px">Do you want to create a CV that stands out from the crowd?</div>
<div class="abs bubble" style="left:98px;top:337px;width:326px">Is your current CV not getting you results?</div>
<div class="abs bubble" style="left:796px;top:337px;width:315px">Do you want to earn more for the job your searching for?</div>

<section>
  <h1 class="abs name">OWEN</h1>
  <div class="abs script">The Harbourlight CV Consultant</div>
  <div class="abs intro">
    <p>If so then invest in a CV writing partnership with Owen, the Harbourlight CV consultant.</p>
    <p>But first read the testimonials. These are real results from real people. They invested in the partnership approach, and they’re delighted because it works. The blurb that follows is not as important as what they say – I’d&nbsp; love it if you were the next person to appear in these testimonials. .</p>
    <p>People I work with get a job sooner and get a higher paid job.</p>
    <p>Working with me is personalised, it’s a partnership. Together we will build a great CV that will present you in the best way possible, it will increase the chances of you securing the job you want.</p>
    <p>And you’ll also get this. As a result of my approach everyone I’ve worked with is better prepared for interview. Our partnership will</p>
  </div>

  <div class="abs pillar" style="left:316px;top:1323px;background:var(--grey-circle)" role="img" aria-label="Icon of a person with arrows pointing inward"></div>
  <div class="abs pillar" style="left:495px;top:1323px;background:var(--slate-circle);opacity:.97" role="img" aria-label="Icon of a group of people with upward arrows"></div>
  <div class="abs pillar" style="left:675px;top:1323px;background:var(--sky-circle);opacity:.95" role="img" aria-label="Icon of a raised fist with a star"></div>
  <div class="abs pillar-label" style="left:337px;top:1556px">Increase self awareness</div>
  <div class="abs pillar-label" style="left:509px;top:1556px">Improve presentation skills</div>
  <div class="abs pillar-label" style="left:681px;top:1556px">Build the right sort of confidence</div>

  <p class="abs outro">And as a result you’ll impress at interview. You’ll develop a language and way of expressing yourself that shows the very best of you. And as that language sinks in and becomes part of you, you project a genuine confidence, quietly powerful, that recruiters will want in their teams.</p>
</section>

<section class="abs band">
  <h2>CLIENT TESTIMONIALS</h2>
  <div class="card" style="left:111px"><q>Lorem ipsum dolor sit ameto ns ectetur adipiscing elit, sed do ei usmod tempor incididunt utore et dolore magna aliqua enim ad minim ven.</q><div class="by"><b>Clara, 7</b> May 2024</div></div>
  <div class="card" style="left:444px"><q>Lorem ipsum dolor sit ameto ns ectetur adipiscing elit, sed do ei usmod tempor incididunt utore et dolore magna aliqua enim ad minim ven.</q><div class="by"><b>Clara, 7</b> May 2024</div></div>
  <div class="card" style="left:777px"><q>Lorem ipsum dolor sit ameto ns ectetur adipiscing elit, sed do ei usmod tempor incididunt utore et dolore magna aliqua enim ad minim ven.</q><div class="by"><b>Clara, 7</b> May 2024</div></div>
  <div class="card" style="left:1107px"><q>Lorem ipsum dolor sit ameto ns ectetur adipiscing elit, sed do ei usmod tempor incididunt utore et dolore magna aliqua enim ad minim ven.</q><div class="by"><b>Clara, 7</b> May 2024</div></div>
  <div class="next"><svg width="14" height="20" viewBox="0 0 14 20"><path d="M3 2l8 8-8 8" fill="none" stroke="#333" stroke-width="2"/></svg></div>
</section>

<section class="abs partner" role="img" aria-label="Photo of a team stacking hands together in the centre">
  <h2>THE PARTNERSHIP</h2>
  <div class="copy">
    <p>The key to all this success is the partnership. Over four sessions we will, together, build a CV. You will get me, no one else, working with you for four sessions. There is a formula for success but it’s not formulaic. Your CV will be personal, you will shine through. Your CV will be elevated above the crowd.</p>
    <p>I offer a premium service, very different to other offerings - so if like those in the testimonials, you get that job sooner, get a higher paid job, the investment is a wise one.</p>
    <p>So take the first step to the best CV you can have.</p>
  </div>
  <div class="abs btn partner-btn">Contact me now</div>
</section>

<footer>
  <div class="abs logo" style="left:112px;top:3058px">THE HARBOURLIGHT<br>CV CONSULTANT</div>
  <div class="abs copyright">© 2024, The Harbourlight CV Consultant. All rights reserved.</div>
  <div class="abs social" style="left:966px;top:3057px" aria-label="Social link"></div>
  <div class="abs social" style="left:1010px;top:3057px" aria-label="Social link"></div>
  <div class="abs social" style="left:1053px;top:3057px" aria-label="Social link"></div>
</footer>

</body>
</html>
```